Business Card for Coach - ready to print

Design Business Card ready to order prints www.lukasbrenner.coach

* An Overview / Background of the Business & Services
· Coaching
· Personal growth
* The Target Market / Audience you are trying to reach
· private person in different roles (self, familiy, business role)s
* Design Specifics; any preferences or ideas for Style, Colour, Imagery, etc
· See www.lukasbrenner.coach
· "simple" design
· (small) element of surprise / unusual element

* Information that will be placed in the Business Card
· Beratung und Coaching
· Address: Lukas Brenner, Talmatt 42, CH-8531 Winterthur, Mobile +41 76 254 63 07
* Do you have an existing website or Facebook page where designers can learn more about your company?
· lukasbrenner.coach

Target Market(s)

private person in different roles (self, familiy, business role)

Industry/Entity Type

Life Coaching

Contact Information for Business Card

Lukas Brenner
Talmatt 42
CH-8531 Winterthur

Mobile: +41 76 254 63 07
Email: lubr@sonnwelt.ch
www.lukasbrenner.coach

Font styles to use
Sans Serif

Colors

Designer to choose colors to be used in the design.

Requirements
Must have
• "simple" design
• element of surprise / unusual element
• Beratung & Coaching
• see www.lukasbrenner.coach for colors and so...
Nice to have
• TA Symbol (three rings on top of each other) - unsual presentation
• QR Code of Website (see if it fits in and still looks good).

```html
<!DOCTYPE html>
<html lang="de">
<head>
<meta charset="utf-8">
<title>Lukas Brenner – Life Coaching Visitenkarte</title>
<link rel="stylesheet" href="https://fonts.googleapis.com/css2?family=Questrial&family=Montserrat:wght@700&display=swap">
<style>
  :root {
    --backdrop: #2b2b2b;
    --card: #ffffff;
    --ink-grey: #4d5057;
    --accent-blue: #5cc8f2;
    --text-dark: #3f4248;
  }
  * { margin: 0; padding: 0; box-sizing: border-box; }
  html, body { width: 1200px; height: 880px; overflow: hidden; }
  body {
    background: var(--backdrop);
    font-family: "Questrial", "Century Gothic", sans-serif;
    position: relative;
  }
  .card {
    position: absolute;
    left: 280px;
    width: 640px;
    height: 412px;
    background: var(--card);
    border-radius: 22px;
  }
  .card--front { top: 22px; }
  .card--back { top: 446px; }

  .front-name {
    position: absolute;
    left: 92px;
    top: 150px;
    font-size: 58px;
    line-height: 1;
    white-space: nowrap;
    letter-spacing: -1px;
  }
  .front-name .first { color: var(--ink-grey); font-family: "Questrial", sans-serif; }
  .front-name .last { color: var(--accent-blue); font-family: "Montserrat", sans-serif; font-weight: 700; }
  .front-tagline {
    position: absolute;
    left: 292px;
    top: 214px;
    font-size: 24px;
    color: var(--accent-blue);
    letter-spacing: 0.5px;
  }

  .back-name {
    position: absolute;
    left: 30px;
    width: 250px;
    top: 62px;
    font-size: 22px;
    line-height: 1;
    white-space: nowrap;
    text-align: right;
    letter-spacing: -0.5px;
  }
  .back-name .first { color: var(--ink-grey); }
  .back-name .last { color: var(--accent-blue); font-family: "Montserrat", sans-serif; font-weight: 700; }
  .divider {
    position: absolute;
    left: 300px;
    top: 40px;
    width: 3px;
    height: 300px;
    background: var(--accent-blue);
  }
  .contact {
    position: absolute;
    left: 336px;
    top: 222px;
    color: var(--text-dark);
    font-size: 15px;
    line-height: 20px;
    white-space: nowrap;
  }
  .contact .address { margin-bottom: 10px; }
  .contact-row { display: flex; align-items: center; gap: 8px; }
  .contact-row svg { width: 13px; height: 13px; flex: none; }
  .contact .domain { font-family: "Montserrat", sans-serif; font-weight: 700; font-size: 14px; }
</style>
</head>
<body>
  <section class="card card--front">
    <div class="front-name"><span class="first">LUKAS </span><span class="last">BRENNER</span></div>
    <div class="front-tagline">Life Coaching</div>
  </section>

  <section class="card card--back">
    <div class="back-name"><span class="first">LUKAS </span><span class="last">BRENNER</span></div>
    <div class="divider"></div>
    <div class="contact">
      <div class="address">Talmatt 42<br>CH-8531 Winterthur</div>
      <div class="contact-row">
        <svg viewBox="0 0 13 13" aria-hidden="true"><rect x="3" y="0.5" width="7" height="12" rx="1.5" fill="none" stroke="#5cc8f2" stroke-width="1.2"/><line x1="5.5" y1="10.5" x2="7.5" y2="10.5" stroke="#5cc8f2" stroke-width="1"/></svg>
        <span>+41 76 254 63 07</span>
      </div>
      <div class="contact-row">
        <svg viewBox="0 0 13 13" aria-hidden="true"><rect x="0.5" y="2.5" width="12" height="8" fill="#5cc8f2"/><polyline points="0.5,2.5 6.5,7 12.5,2.5" fill="none" stroke="#ffffff" stroke-width="1"/></svg>
        <span>lubr@sonnwelt.ch</span>
      </div>
      <div class="contact-row">
        <svg viewBox="0 0 13 13" aria-hidden="true"><circle cx="6.5" cy="6.5" r="5.8" fill="#5cc8f2"/><ellipse cx="6.5" cy="6.5" rx="2.4" ry="5.8" fill="none" stroke="#ffffff" stroke-width="0.8"/><line x1="0.7" y1="6.5" x2="12.3" y2="6.5" stroke="#ffffff" stroke-width="0.8"/></svg>
        <span>www.<span class="domain">lukasbrenner</span>.coach</span>
      </div>
    </div>
  </section>
</body>
</html>
```